Halvorn - Refresh the look and feel of an existing website

We currently have an existing website www.halvornworldadvisory.example however it needs a more refreshed 'look and feel'. We are a professional consultancy that works with large corporate organisations and government. Our 'tag line' is A New Way of Thinking. We want the site to communicate "Innovation" and Leading Edge Thinking.

Target Market(s)

Corporate and Professional Clients - Organisation and Business Change

Industry/Entity Type

Management Consulting

Number of Pages Required

1 page

Font styles to use
Sans Serif

Requirements
Must have
• Must have a professional Corporate look and feel. Header 'imagery' is ok but boxes on front page need changing ... along with the words. The focus on home page needs to 'call out' 3 main consulting areas:-
• - Change & Transformation Specialists
• - Innovative Solutions
• - Digital Transformation
• Tag Line for business is ... A New Way of Thinking (Highlighting Halvorn as 'Thought Leaders' in business)
Nice to have
• Less "words' more imagery. Possibly an area for a 'video' or recent articles/blogs on the front page. Needs to have more of an 'interactive' feel. We are open to suggestions.
Should not have
• NA

```html
<!DOCTYPE html>
<html lang="en">
<head>
<meta charset="utf-8">
<title>Halvorn World Advisory</title>
<link href="https://fonts.googleapis.com/css2?family=Open+Sans:wght@300;400;600;700&display=swap" rel="stylesheet">
<style>
:root{
  --topbar:#2e2e2e;
  --navy:#2b3a5c;
  --navy-deep:#243956;
  --accent:#56658a;
  --button:#4a5678;
  --footer-dark:#262626;
  --text:#5e6270;
  --heading:#3f4456;
  --muted:#7a86a0;
  --white:#ffffff;
}
*{box-sizing:border-box;margin:0;padding:0}
html,body{width:734px;height:1200px;overflow:hidden;background:var(--white)}
body{position:relative;font-family:"Open Sans",Arial,sans-serif;color:var(--text)}
.abs{position:absolute}
.topbar{left:0;top:0;width:734px;height:30px;background:var(--topbar);color:#e6e6e6;font-size:9px;font-weight:600}
.topbar .item{top:9px;display:flex;align-items:center;gap:6px}
.social{top:10px;width:10px;height:10px;border-radius:50%;background:#9a9a9a}
.header{left:0;top:30px;width:734px;height:74px;background:var(--navy)}
.brand{left:41px;top:18px;display:flex;align-items:center;gap:8px;color:var(--white)}
.brand-mark{width:34px;height:34px;border-radius:50%;border:3px solid var(--white)}
.brand-text{display:flex;flex-direction:column}
.brand-name{font-size:17px;font-weight:600;letter-spacing:.5px;line-height:19px}
.tagline{font-size:7px;font-weight:600;letter-spacing:.6px;line-height:10px;text-transform:uppercase}
.nav{top:39px;color:var(--white);font-size:9px;font-weight:600;letter-spacing:.2px}
.hero{left:0;top:104px;width:734px;height:223px;background:linear-gradient(100deg,#8a7a70 0%,#6f7478 35%,#5d6d7c 60%,#8c96a0 80%,#7a6f6a 100%)}
.hero h1{position:absolute;left:79px;top:40px;color:var(--white);font-weight:400;font-size:30px;line-height:31px}
.hero p{position:absolute;left:79px;top:141px;color:var(--white);font-size:11.5px;font-weight:600;line-height:13px}
.btn-hero{position:absolute;left:78px;top:178px;width:77px;height:20px;background:#3d5089;color:var(--white);font-size:9.5px;display:flex;align-items:center;justify-content:center;border-radius:2px}
.section-title{left:0;width:734px;text-align:center}
.what-title{top:350px;font-size:19px;font-weight:300;color:var(--muted)}
.what-intro{left:88px;top:384px;width:558px;text-align:center;font-size:9px;line-height:13.5px}
.service-title{top:452px;font-size:9px;font-weight:700;letter-spacing:.6px;color:var(--heading);white-space:nowrap}
.service-text{top:483px;width:138px;font-size:8.8px;line-height:14.7px}
.service-icon{top:485px}
.btn-small{width:68px;height:19px;background:var(--button);color:var(--white);font-size:7.5px;font-weight:700;display:flex;align-items:center;justify-content:center}
.blog-title{top:632px;font-size:14px;font-weight:600;color:var(--heading);letter-spacing:.3px}
.card-image{top:678px;width:205px;height:187px}
.date-box{top:683px;width:67px;height:114px;background:var(--accent);color:var(--white);font-size:13px;font-weight:600;text-align:center;line-height:26px;padding-top:18px}
.card-title{top:880px;font-size:9.5px;font-weight:700;color:var(--heading)}
.card-text{top:900px;width:205px;font-size:9px;line-height:14px}
.btn-view{top:953px;width:86px;height:31px;background:var(--button);color:var(--white);font-size:9.5px;display:flex;align-items:center;justify-content:center}
.footer{left:0;top:1021px;width:734px;height:156px;background:var(--footer-dark)}
.footer-brand{left:0;top:1021px;width:211px;height:156px;background:var(--navy-deep)}
.footer-brand .brand{left:41px;top:58px}
.footer-text{font-size:9px;color:#b8bcc4;line-height:13px}
.footer-link{display:flex;align-items:center;gap:9px;font-size:9px;color:#b8bcc4}
.copyright{left:0;top:1177px;width:734px;height:23px;background:var(--navy-deep);color:#7f8aa6;font-size:9px;text-align:center;line-height:23px}
</style>
</head>
<body>

<div class="abs topbar">
  <div class="abs item" style="left:45px">
    <svg width="9" height="9" viewBox="0 0 24 24"><path fill="#e6e6e6" d="M6.6 10.8a15 15 0 0 0 6.6 6.6l2.2-2.2c.3-.3.7-.4 1-.2 1.1.4 2.3.6 3.6.6.6 0 1 .4 1 1V20c0 .6-.4 1-1 1C10.6 21 3 13.4 3 4c0-.6.4-1 1-1h3.5c.6 0 1 .4 1 1 0 1.3.2 2.5.6 3.6.1.3 0 .7-.2 1z"/></svg>
    <span>(+613) 9555 0142</span>
  </div>
  <div class="abs item" style="left:188px">
    <svg width="10" height="8" viewBox="0 0 20 16"><rect width="20" height="16" fill="#e6e6e6"/><path d="M0 0l10 8 10-8" stroke="#2e2e2e" stroke-width="2" fill="none"/></svg>
    <span>info@halvornworldadvisory.example</span>
  </div>
  <span class="abs social" style="left:570px"></span>
  <span class="abs social" style="left:602px"></span>
  <span class="abs social" style="left:636px"></span>
  <span class="abs social" style="left:670px"></span>
</div>

<header class="abs header">
  <div class="abs brand"><span class="brand-mark"></span><span class="brand-text"><span class="brand-name">HALVORN</span><span class="tagline">A New Way of Thinking</span></span></div>
  <span class="abs nav" style="left:267px">Home</span>
  <span class="abs nav" style="left:318px">About Us</span>
  <span class="abs nav" style="left:383px">Our Services</span>
  <span class="abs nav" style="left:463px">Solutions</span>
  <span class="abs nav" style="left:526px">What's Happening</span>
  <span class="abs nav" style="left:632px">Contact Us</span>
</header>

<section class="abs hero" role="img" aria-label="Photograph of an angular triangulated glass and stone facade">
  <h1>We specialise in<br>working with<br>complex problems.</h1>
  <p>Our agility and expertise allow us to<br>arrive at the right solution - quickly.</p>
  <span class="btn-hero">LEARN MORE</span>
</section>

<h2 class="abs section-title what-title">What We Do</h2>
<p class="abs what-intro">Nulla ut semper augue, eget euismod quam. Quisque vel ligula nunc. Suspendisse eleifend massa molestieNulla ut semper augue, eget euismod quam. Quisque vel ligula nunc. Suspendisse eleifend massa molestie</p>

<h3 class="abs service-title" style="left:45px">CHANGE &amp; TRANSFORMATION SPECIALISTS</h3>
<h3 class="abs service-title" style="left:284px">INNOVATIVE SOLUTIONS</h3>
<h3 class="abs service-title" style="left:508px">DIGITAL TRANSFORMATION</h3>

<svg class="abs service-icon" style="left:25px;top:483px" width="50" height="40" viewBox="0 0 50 40">
  <rect x="0" y="4" width="50" height="36" fill="#f2f2f2"/>
  <rect x="20" y="10" width="18" height="14" fill="none" stroke="#555" stroke-width="1.5"/>
  <rect x="23" y="13" width="12" height="8" fill="none" stroke="#555" stroke-width="1"/>
</svg>
<svg class="abs service-icon" style="left:285px" width="28" height="30" viewBox="0 0 28 30">
  <circle cx="14" cy="13" r="6.5" fill="none" stroke="#555" stroke-width="1.5"/>
  <path d="M11 20h6v5h-6z" fill="none" stroke="#555" stroke-width="1.5"/>
  <path d="M14 2v2M4 6l2 2M24 6l-2 2M1 14h2M25 14h2" stroke="#555" stroke-width="1.5"/>
</svg>
<svg class="abs service-icon" style="left:512px" width="22" height="28" viewBox="0 0 22 28">
  <circle cx="9" cy="7" r="6" fill="none" stroke="#777" stroke-width="1.5"/>
  <rect x="7" y="5" width="4" height="14" rx="2" fill="#777"/>
  <rect x="6" y="15" width="12" height="12" rx="3" fill="#777"/>
</svg>

<p class="abs service-text" style="left:92px">Nulla ut semper augue, eget euismod quam. Quisque vel ligula nunc. Suspendisse eleif-end massa molestie</p>
<p class="abs service-text" style="left:327px">Nulla ut semper augue, eget euismod quam. Quisque vel ligula nunc. Suspendisse eleif-end massa molestie</p>
<p class="abs service-text" style="left:550px">Nulla ut semper augue, eget euismod quam. Quisque vel ligula nunc. Suspendisse eleif-end massa molestie</p>

<span class="abs btn-small" style="left:92px;top:557px">Read more</span>
<span class="abs btn-small" style="left:328px;top:558px">Read more</span>
<span class="abs btn-small" style="left:550px;top:559px">Read more</span>

<h2 class="abs section-title blog-title">Latest post on our Blog</h2>

<div class="abs card-image" style="left:41px;background:linear-gradient(135deg,#c9b08a,#e8e4dc 50%,#8fa6b8)" role="img" aria-label="Photograph of a hand sketching a business plan on paper"></div>
<div class="abs card-image" style="left:259px;background:linear-gradient(135deg,#9a9a9a,#dcdcdc 50%,#b9a58c)" role="img" aria-label="Photograph of a hand placing a block on a wooden tower"></div>
<div class="abs card-image" style="left:478px;background:linear-gradient(180deg,#4f6f9a,#9bb4cf 50%,#d9c7a0 75%,#5c6a80)" role="img" aria-label="Photograph of a meeting room silhouetted against a bright window"></div>

<div class="abs date-box" style="left:41px">JAN<br>06<br>2016</div>
<div class="abs date-box" style="left:259px">JAN<br>06<br>2016</div>
<div class="abs date-box" style="left:478px">JAN<br>06<br>2016</div>

<h4 class="abs card-title" style="left:42px">Nulla ut semper augue, eget.</h4>
<h4 class="abs card-title" style="left:260px;top:885px">Nulla ut semper augue, eget.</h4>
<h4 class="abs card-title" style="left:479px;top:889px">Nulla ut semper augue, eget.</h4>

<p class="abs card-text" style="left:42px">Nulla ut semper augue, eget euismod quam. Quisque vel ligula nunc. Suspendisse eleif-end massa molestie</p>
<p class="abs card-text" style="left:260px;top:905px">Nulla ut semper augue, eget euismod quam. Quisque vel ligula nunc. Suspendisse eleif-end massa molestie</p>
<p class="abs card-text" style="left:479px;top:909px">Nulla ut semper augue, eget euismod quam. Quisque vel ligula nunc. Suspendisse eleif-end massa molestie</p>

<span class="abs btn-view" style="left:42px">View More</span>
<span class="abs btn-view" style="left:260px;top:958px">View More</span>
<span class="abs btn-view" style="left:479px;top:962px">View More</span>

<footer>
  <div class="abs footer"></div>
  <svg class="abs" style="left:211px;top:1120px" width="50" height="57" viewBox="0 0 50 57">
    <path d="M0 0 C4 30 10 50 50 57 L0 57 Z" fill="#ffffff"/>
  </svg>
  <div class="abs footer-brand">
    <div class="abs brand"><span class="brand-mark"></span><span class="brand-text"><span class="brand-name">HALVORN</span><span class="tagline">A New Way of Thinking</span></span></div>
  </div>

  <svg class="abs" style="left:238px;top:1044px" width="8" height="10" viewBox="0 0 12 16"><path d="M6 0a6 6 0 0 1 6 6c0 4-6 10-6 10S0 10 0 6a6 6 0 0 1 6-6z" fill="#8a8f99"/><circle cx="6" cy="6" r="2" fill="#262626"/></svg>
  <p class="abs footer-text" style="left:258px;top:1042px">PO Box 418<br>Larkspur Lane West<br>Victoria 8090<br>AUSTRALIA</p>

  <svg class="abs" style="left:238px;top:1114px" width="9" height="9" viewBox="0 0 24 24"><path fill="#8a8f99" d="M6.6 10.8a15 15 0 0 0 6.6 6.6l2.2-2.2c.3-.3.7-.4 1-.2 1.1.4 2.3.6 3.6.6.6 0 1 .4 1 1V20c0 .6-.4 1-1 1C10.6 21 3 13.4 3 4c0-.6.4-1 1-1h3.5c.6 0 1 .4 1 1 0 1.3.2 2.5.6 3.6.1.3 0 .7-.2 1z"/></svg>
  <p class="abs footer-text" style="left:257px;top:1112px;line-height:19px">1300 555 218 (Aus)<br>0800 555 218 (NZ)<br>1300 555 219 (Intl)</p>

  <div class="abs footer-link" style="left:406px;top:1045px"><svg width="8" height="7" viewBox="0 0 10 8"><path d="M1 4l3 3 5-6" stroke="#c9ced8" stroke-width="1.8" fill="none"/></svg>Our Team</div>
  <div class="abs footer-link" style="left:406px;top:1067px"><svg width="8" height="7" viewBox="0 0 10 8"><path d="M1 4l3 3 5-6" stroke="#c9ced8" stroke-width="1.8" fill="none"/></svg>Our Values</div>
  <div class="abs footer-link" style="left:406px;top:1089px"><svg width="8" height="7" viewBox="0 0 10 8"><path d="M1 4l3 3 5-6" stroke="#c9ced8" stroke-width="1.8" fill="none"/></svg>Giving Back</div>

  <div class="abs footer-link" style="left:535px;top:1043px"><svg width="8" height="7" viewBox="0 0 10 8"><path d="M1 4l3 3 5-6" stroke="#c9ced8" stroke-width="1.8" fill="none"/></svg>Strategy and Design</div>
  <div class="abs footer-link" style="left:535px;top:1065px"><svg width="8" height="7" viewBox="0 0 10 8"><path d="M1 4l3 3 5-6" stroke="#c9ced8" stroke-width="1.8" fill="none"/></svg>Transformation</div>
  <div class="abs footer-link" style="left:535px;top:1087px"><svg width="8" height="7" viewBox="0 0 10 8"><path d="M1 4l3 3 5-6" stroke="#c9ced8" stroke-width="1.8" fill="none"/></svg>Change &amp; Culture</div>
  <div class="abs footer-link" style="left:535px;top:1109px"><svg width="8" height="7" viewBox="0 0 10 8"><path d="M1 4l3 3 5-6" stroke="#c9ced8" stroke-width="1.8" fill="none"/></svg>Organisational Development</div>
  <div class="abs footer-link" style="left:535px;top:1131px"><svg width="8" height="7" viewBox="0 0 10 8"><path d="M1 4l3 3 5-6" stroke="#c9ced8" stroke-width="1.8" fill="none"/></svg>Project Management</div>
  <div class="abs footer-link" style="left:535px;top:1153px"><svg width="8" height="7" viewBox="0 0 10 8"><path d="M1 4l3 3 5-6" stroke="#c9ced8" stroke-width="1.8" fill="none"/></svg>Organisational Efficiency</div>

  <div class="abs copyright">Copyright © 2016 Halvorn World Advisory</div>
</footer>

</body>
</html>
```